Playing Card Design for Magician's Business Card

Hello! I am looking for a two-sided design for a business card.
The back of the card look like the back of a playing card and includes the following text:
Desmond Halloway
www.TrickvaleShows.com
BACK:
Please - focus most of your time and effort on the BACK DESIGN.
Make it look like a playing card.
I plan to use this design to print up custom playing cards that I use in my show and give away to guests.
No Bunnies No Top Hats!
Not for kids. This is for sophisticated sleight of hand performed for adults.
Mood: Slick, elegant + fun.
See the attached samples of cards I like.
FRONT:
Not much text required ... Please leave plenty of blank space - minimalist.
The front of the card will have
First Name
Website
Phone Number
Email Address
Target Market(s)
Event Planners
Targeting corporate special events and private parties.
Industry/Entity Type
Magician
Contact Information for Business Card
Desmond Halloway
Illusionist
www.TrickvaleShows.com
Colors
Designer to choose colors to be used in the design.
Requirements
Must have
- Back must look like a playing card back.
- BACK MUST INCLUDE the following text:
- Desmond Halloway
- www.TrickvaleShows.com
Nice to have
- Symmetrical Design for back so the card looks the same if upside down.
- Please see "All Seeing Eye" design attached. Remove the Latin phrase and replace with Desmond (top left) Halloway (top right)
- TrickvaleShows.com (Lower middle)
Should not have
- Bunny Rabbits
- Top Hats
- Kids ....

```html
<!DOCTYPE html>
<html lang="en">
<head>
<meta charset="utf-8">
<title>Desmond Halloway – Business Card</title>
<link rel="stylesheet" href="https://fonts.googleapis.com/css2?family=Playfair+Display:wght@400;600&family=Libre+Baskerville:wght@400;700&display=swap">
<style>
  :root {
    --paper: #ffffff;
    --card-black: #000000;
    --gold: #e2b24e;
    --ink-white: #ffffff;
    --title-gold: #c9a04a;
  }
  html, body {
    margin: 0;
    padding: 0;
    width: 958px;
    height: 1200px;
    overflow: hidden;
    background: var(--paper);
  }
  .canvas {
    position: relative;
    width: 958px;
    height: 1200px;
  }
  .card {
    position: absolute;
    top: 125px;
    width: 231px;
    height: 405px;
    background: var(--card-black);
  }
  .card--back { left: 194px; }
  .card--front { left: 542px; }
  .card svg { position: absolute; inset: 0; }

  .front-text {
    position: absolute;
    left: 0;
    width: 100%;
    margin: 0;
    text-align: center;
    white-space: nowrap;
  }
  .front-name {
    top: 153px;
    font-family: "Playfair Display", serif;
    font-weight: 600;
    font-size: 21px;
    color: var(--ink-white);
  }
  .front-title {
    top: 181px;
    font-family: "Playfair Display", serif;
    font-weight: 400;
    font-size: 14.5px;
    letter-spacing: 0.5px;
    color: var(--title-gold);
  }
  .front-web {
    top: 262px;
    font-family: "Libre Baskerville", serif;
    font-weight: 700;
    font-size: 10px;
    letter-spacing: 0.8px;
    color: var(--ink-white);
  }
  .front-phone {
    top: 283px;
    font-family: "Libre Baskerville", serif;
    font-size: 11px;
    letter-spacing: 0.8px;
    color: var(--ink-white);
  }
  .front-email {
    top: 299px;
    font-family: "Libre Baskerville", serif;
    font-size: 10px;
    letter-spacing: 0.4px;
    color: var(--ink-white);
  }
  .emblem-text {
    font-family: "Playfair Display", serif;
    font-weight: 600;
    fill: var(--gold);
    letter-spacing: 1px;
  }
  .emblem-name { font-size: 15px; }
  .emblem-web { font-size: 11px; letter-spacing: 0.6px; }
</style>
</head>
<body>
<main class="canvas">

  <section class="card card--back" aria-label="Card back">
    <svg width="231" height="405" viewBox="0 0 231 405">
      <g fill="none" stroke="var(--gold)">
        <rect class="frame-outer" x="15.5" y="16" width="199.5" height="374" stroke-width="3.5"/>
        <rect class="frame-second" x="20.5" y="21" width="189.5" height="363.5" stroke-width="2.2"/>
        <rect class="frame-band" x="30" y="30.6" width="171" height="343.5" stroke-width="1.4"/>
        <rect class="frame-panel" x="42.3" y="41.8" width="146.4" height="321.8" rx="8" stroke-width="1.6"/>
        <line class="corner-rule" x1="30" y1="30.6" x2="42.3" y2="49"/>
        <line class="corner-rule" x1="201" y1="30.6" x2="188.7" y2="49"/>
        <line class="corner-rule" x1="30" y1="374" x2="42.3" y2="356"/>
        <line class="corner-rule" x1="201" y1="374" x2="188.7" y2="356"/>
      </g>
      <g class="corner-sparkles" fill="var(--gold)">
        <path d="M41.8 32 Q43 38.5 49 40 Q43 41.5 41.8 48 Q40.6 41.5 34.6 40 Q40.6 38.5 41.8 32Z"/>
        <path d="M189.2 32 Q190.4 38.5 196.4 40 Q190.4 41.5 189.2 48 Q188 41.5 182 40 Q188 38.5 189.2 32Z"/>
        <path d="M41.8 357 Q43 363.5 49 365 Q43 366.5 41.8 373 Q40.6 366.5 34.6 365 Q40.6 363.5 41.8 357Z"/>
        <path d="M189.2 357 Q190.4 363.5 196.4 365 Q190.4 366.5 189.2 373 Q188 366.5 182 365 Q188 363.5 189.2 357Z"/>
      </g>
      <g class="emblem emblem--top">
        <circle cx="115.8" cy="115.2" r="71" fill="none" stroke="var(--gold)" stroke-width="2.2"/>
        <text class="emblem-text emblem-name" x="115.8" y="100" text-anchor="middle">Desmond</text>
        <text class="emblem-text emblem-name" x="115.8" y="120" text-anchor="middle">Halloway</text>
        <text class="emblem-text emblem-web" x="115.8" y="152" text-anchor="middle">TrickvaleShows.com</text>
      </g>
      <g class="emblem emblem--bottom" transform="rotate(180 115.8 289.5)">
        <circle cx="115.8" cy="289.5" r="71" fill="none" stroke="var(--gold)" stroke-width="2.2"/>
        <text class="emblem-text emblem-name" x="115.8" y="274.3" text-anchor="middle">Desmond</text>
        <text class="emblem-text emblem-name" x="115.8" y="294.3" text-anchor="middle">Halloway</text>
        <text class="emblem-text emblem-web" x="115.8" y="326.3" text-anchor="middle">TrickvaleShows.com</text>
      </g>
    </svg>
  </section>

  <section class="card card--front" aria-label="Card front">
    <svg width="231" height="405" viewBox="0 0 231 405" aria-hidden="true">
      <g class="corner-sparkles" fill="var(--gold)">
        <path d="M41.8 31 Q43.3 40.3 52.6 41.8 Q43.3 43.3 41.8 52.6 Q40.3 43.3 31 41.8 Q40.3 40.3 41.8 31Z"/>
        <path d="M190 31 Q191.5 40.3 200.8 41.8 Q191.5 43.3 190 52.6 Q188.5 43.3 179.2 41.8 Q188.5 40.3 190 31Z"/>
        <path d="M41.8 353.8 Q43.3 363.1 52.6 364.6 Q43.3 366.1 41.8 375.4 Q40.3 366.1 31 364.6 Q40.3 363.1 41.8 353.8Z"/>
        <path d="M190 353.8 Q191.5 363.1 200.8 364.6 Q191.5 366.1 190 375.4 Q188.5 366.1 179.2 364.6 Q188.5 363.1 190 353.8Z"/>
      </g>
    </svg>
    <h1 class="front-text front-name">Desmond Halloway</h1>
    <p class="front-text front-title">Illusionist</p>
    <p class="front-text front-web">www.trickvaleshows.com</p>
    <p class="front-text front-phone">212-555-0187</p>
    <p class="front-text front-email">desmond@trickvaleshows.com</p>
  </section>

</main>
</body>
</html>
```